Spring Detox sale graphics for social media

You MUST read the Brief in the WORD document and follow the instructions there. I want to create 10 social media graphics (new Instagram size 4:5 (1080 x 1350 pixels) focusing on our Mother’s Day Spring Detox Sale graphics, using any of the pics attached. Use the attached pics, NO RANDOM STOCK PHOTOGRAPHY. For the color scheme of the graphics, they should all be complementary to the product colors or feel like Spring time.

Target Market(s)

primarily women

Requirements
Must have
• the photos and text attached

```html
<!DOCTYPE html>
<html lang="en">
<head>
<meta charset="utf-8">
<title>Mother's Day Spring Detox Sale – Social Set</title>
<link rel="stylesheet" href="https://fonts.googleapis.com/css2?family=Anton&family=Archivo+Black&family=Bebas+Neue&family=Playfair+Display:ital,wght@0,900;1,900&family=Poppins:ital,wght@0,500;0,600;0,800;0,900;1,800&display=swap">
<style>
  :root{
    --canvas:#ffffff;
    --mint-light:#eef7f3;
    --mint:#cfe7dd;
    --mint-mid:#a9d5c4;
    --green-dark:#2a5a4b;
    --green:#2f7d65;
    --pink:#b94f86;
    --pink-soft:#f2a3cf;
    --pink-hl:rgba(240,140,200,.75);
    --white:#ffffff;
    --photo-a:#f4f6f5;
    --photo-b:#d9dedc;
  }
  *{margin:0;padding:0;box-sizing:border-box}
  html,body{width:1200px;height:608px;overflow:hidden;background:var(--canvas)}
  .board{position:relative;width:1200px;height:608px}
  .panel{position:absolute;width:230px;height:288px;overflow:hidden;
    background:radial-gradient(ellipse at 50% 35%,var(--mint-light) 0%,#e2f1eb 50%,var(--mint) 100%)}
  .row-1{top:14px}.row-2{top:306px}
  .col-1{left:15px}.col-2{left:250px}.col-3{left:485px}.col-4{left:719px}.col-5{left:954px}

  .line{position:absolute;left:0;right:0;text-align:center;white-space:nowrap;line-height:1}
  .script-sans{font-family:'Poppins',sans-serif;font-style:italic;font-weight:800;color:var(--green-dark);letter-spacing:-.5px}
  .serif-spring{font-family:'Playfair Display',serif;font-weight:900;color:var(--pink);transform:scaleX(.78);letter-spacing:-2px}
  .off-head{font-family:'Poppins',sans-serif;font-weight:900;color:var(--green-dark);letter-spacing:-1px}
  .serif-italic{font-family:'Playfair Display',serif;font-style:italic;font-weight:900;color:var(--green-dark);letter-spacing:-1px}
  .highlight{position:absolute;background:var(--pink-hl);border-radius:2px}
  .condensed{font-family:'Bebas Neue',sans-serif;color:var(--pink-soft)}
  .wide{font-family:'Archivo Black',sans-serif;color:var(--white);letter-spacing:4px}
  .tagline{font-family:'Poppins',sans-serif;font-weight:600;color:var(--green-dark)}
  .heavy{font-family:'Archivo Black',sans-serif}
  .slant{font-family:'Anton',sans-serif;transform:skewX(-9deg);letter-spacing:-.5px}

  .arch{position:absolute;border-radius:999px 999px 0 0;background:var(--green-dark)}
  .arch.ring{background:var(--mint-mid);border:9px solid var(--green-dark);border-bottom:0}
  .arch.halo{background:var(--mint-mid)}
  .photo{position:absolute;border-radius:40px 40px 4px 4px;
    background:linear-gradient(180deg,var(--photo-a) 0%,#e6ebe9 55%,var(--photo-b) 100%)}
  .ribbon{position:absolute;left:20px;width:190px}
  .ribbon svg{display:block;width:100%;height:100%}
  .ribbon .ribbon-text{position:absolute;inset:0;display:flex;flex-direction:column;align-items:center;justify-content:center;text-align:center;line-height:1}

  .tag{position:absolute;left:74px;width:84px;height:12px;background:var(--pink);color:var(--white);
    font-family:'Poppins',sans-serif;font-weight:600;font-size:9px;line-height:12px;text-align:center}

  .big-25{position:absolute;font-family:'Poppins',sans-serif;font-weight:900;line-height:.8;letter-spacing:-4px}
  .pct{position:absolute;font-family:'Poppins',sans-serif;font-weight:900;line-height:.8}
  .off-small{position:absolute;font-family:'Poppins',sans-serif;font-weight:900;line-height:1}
  .pink-box{position:absolute;background:var(--pink);display:flex;align-items:center;justify-content:center}
</style>
</head>
<body>
<main class="board">

  <!-- 1 -->
  <section class="panel row-1 col-1">
    <div class="line script-sans" style="top:29px;font-size:19px">Mother’s Day</div>
    <div class="line serif-spring" style="top:30px;font-size:66px">SPRING</div>
    <div class="arch" style="left:46px;top:136px;width:138px;height:100px"></div>
    <div class="photo" role="img" aria-label="Smiling woman in white cropped sweater standing behind a row of supplement bottles" style="left:55px;top:92px;width:122px;height:140px"></div>
    <div class="ribbon" style="top:229px;height:40px">
      <svg viewBox="0 0 190 40" preserveAspectRatio="none"><polygon points="0,0 190,0 182,20 190,40 0,40 8,20" fill="var(--green-dark)"/></svg>
      <div class="ribbon-text" style="font-family:'Poppins',sans-serif;font-weight:500;color:var(--white);font-size:13px;gap:3px">
        <span>DETOX SALE</span><span style="font-size:12.5px">25% Off Everything!</span>
      </div>
    </div>
  </section>

  <!-- 2 -->
  <section class="panel row-1 col-2">
    <div class="line off-head" style="top:10px;font-size:44px">25% Off</div>
    <div class="highlight" style="left:17px;top:66px;width:198px;height:15px"></div>
    <div class="line serif-italic" style="top:50px;font-size:33px">Mother’s Day</div>
    <div class="arch halo" style="left:40px;top:116px;width:150px;height:120px"></div>
    <div class="arch" style="left:48px;top:126px;width:134px;height:110px"></div>
    <div class="photo" role="img" aria-label="Smiling woman in white cropped sweater standing behind a row of supplement bottles" style="left:55px;top:88px;width:122px;height:144px"></div>
    <div class="ribbon" style="top:232px;height:40px">
      <svg viewBox="0 0 190 40" preserveAspectRatio="none"><polygon points="0,0 190,0 182,20 190,40 0,40 8,20" fill="var(--green-dark)"/></svg>
      <div class="ribbon-text wide" style="font-size:32px">SALE</div>
    </div>
    <div class="tag" style="top:225px">SPRING DETOX</div>
  </section>

  <!-- 3 -->
  <section class="panel row-1 col-3">
    <div class="line off-head" style="top:10px;font-size:44px">25% Off</div>
    <div class="highlight" style="left:16px;top:66px;width:200px;height:15px"></div>
    <div class="line serif-italic" style="top:52px;font-size:29px">All Supplements</div>
    <div class="arch" style="left:48px;top:126px;width:134px;height:110px"></div>
    <div class="photo" role="img" aria-label="Smiling woman in white cropped sweater standing behind a row of supplement bottles" style="left:55px;top:88px;width:122px;height:144px"></div>
    <div class="ribbon" style="top:232px;height:40px">
      <svg viewBox="0 0 190 40" preserveAspectRatio="none"><polygon points="0,0 190,0 182,20 190,40 0,40 8,20" fill="var(--green-dark)"/></svg>
      <div class="ribbon-text condensed" style="font-size:30px">SPRING DETOX SALE</div>
    </div>
  </section>

  <!-- 4 -->
  <section class="panel row-1 col-4">
    <div class="line off-head" style="top:16px;font-size:28px;color:var(--green)">25% Off</div>
    <div class="line serif-spring" style="top:32px;font-size:64px">SPRING</div>
    <div class="arch ring" style="left:47px;top:120px;width:136px;height:110px"></div>
    <div class="photo" role="img" aria-label="Smiling woman in white cropped sweater standing behind a row of supplement bottles" style="left:55px;top:90px;width:122px;height:138px"></div>
    <div class="ribbon" style="top:219px;height:40px">
      <svg viewBox="0 0 190 40" preserveAspectRatio="none"><polygon points="0,0 190,0 182,20 190,40 0,40 8,20" fill="var(--green-dark)"/></svg>
      <div class="ribbon-text condensed" style="font-size:36px">DETOX SALE</div>
    </div>
    <div class="line tagline" style="top:266px;font-size:11.5px">Spring Reset. Summer Ready.</div>
  </section>

  <!-- 5 -->
  <section class="panel row-1 col-5">
    <div class="line off-head" style="top:10px;font-size:44px">25% Off</div>
    <div class="line serif-italic" style="top:50px;font-size:37px">Everything</div>
    <div class="arch" style="left:48px;top:116px;width:134px;height:100px"></div>
    <div class="photo" role="img" aria-label="Smiling woman in white cropped sweater standing behind a row of supplement bottles" style="left:55px;top:88px;width:122px;height:126px"></div>
    <div class="ribbon" style="top:211px;height:40px">
      <svg viewBox="0 0 190 40" preserveAspectRatio="none"><polygon points="0,0 190,0 182,20 190,40 0,40 8,20" fill="var(--green-dark)"/></svg>
      <div class="ribbon-text condensed" style="font-size:36px">MOTHER’S DAY</div>
    </div>
    <div class="line tagline" style="top:257px;font-size:15px;font-weight:500">Spring Detox Sale</div>
  </section>

  <!-- 6 -->
  <section class="panel row-2 col-1">
    <div class="line off-head" style="top:12px;font-size:44px">25% Off</div>
    <div class="highlight" style="left:17px;top:68px;width:198px;height:15px"></div>
    <div class="line serif-italic" style="top:52px;font-size:33px">Mother’s Day</div>
    <div class="arch ring" style="left:47px;top:120px;width:136px;height:100px"></div>
    <div class="photo" role="img" aria-label="Smiling woman in white cropped sweater standing behind a row of supplement bottles" style="left:55px;top:86px;width:122px;height:132px"></div>
    <div class="ribbon" style="top:217px;height:40px">
      <svg viewBox="0 0 190 40" preserveAspectRatio="none"><polygon points="0,0 190,0 182,20 190,40 0,40 8,20" fill="var(--green-dark)"/></svg>
      <div class="ribbon-text wide" style="font-size:32px;color:var(--pink-soft)">SALE</div>
    </div>
    <div class="line tagline" style="top:260px;font-size:13.5px;font-weight:500">Feel Amazing Again</div>
  </section>

  <!-- 7 -->
  <section class="panel row-2 col-2">
    <div class="big-25" style="left:18px;top:21px;font-size:104px;color:var(--green)">25</div>
    <div class="pct" style="left:152px;top:21px;font-size:58px;color:var(--green)">%</div>
    <div class="off-small" style="left:152px;top:75px;font-size:26px;color:var(--green)">OFF</div>
    <div class="line off-head" style="top:102px;font-size:18.5px;letter-spacing:-.5px">MOTHER’S DAY SALE</div>
    <div class="line heavy" style="top:120px;font-size:38px;color:var(--pink);letter-spacing:-1px">REFRESH</div>
    <div class="line heavy" style="top:154px;font-size:31px;color:var(--green-dark);letter-spacing:-1px">YOUR BODY</div>
    <div class="photo" role="img" aria-label="Four white supplement bottles with coloured labels in a row" style="left:19px;top:194px;width:197px;height:84px;border-radius:8px"></div>
  </section>

  <!-- 8 -->
  <section class="panel row-2 col-3">
    <div class="big-25" style="left:18px;top:21px;font-size:104px;color:var(--green-dark)">25</div>
    <div class="pct" style="left:152px;top:21px;font-size:58px;color:var(--green-dark)">%</div>
    <div class="off-small" style="left:152px;top:75px;font-size:26px;color:var(--green-dark)">OFF</div>
    <div class="line slant" style="top:98px;font-size:62px;color:var(--green)">SPRING</div>
    <div class="pink-box" style="left:17px;top:167px;width:196px;height:34px">
      <span class="serif-italic" style="color:var(--white);font-size:31px;line-height:1">Detox Sale</span>
    </div>
    <div class="line slant" style="top:205px;font-size:21px;color:var(--green-dark)">THIS SPRING SHINE LIKE</div>
    <div class="line heavy" style="top:226px;font-size:40px;color:var(--green);letter-spacing:-1px">SUMMER</div>
  </section>

  <!-- 9 -->
  <section class="panel row-2 col-4">
    <div class="big-25" style="left:18px;top:21px;font-size:104px;color:var(--green)">25</div>
    <div class="pct" style="left:152px;top:21px;font-size:58px;color:var(--green)">%</div>
    <div class="off-small" style="left:152px;top:75px;font-size:26px;color:var(--green)">OFF</div>
    <div class="line slant" style="top:104px;font-size:38px;color:var(--green-dark)">MOTHER’S DAY</div>
    <div class="pink-box" style="left:17px;top:143px;width:199px;height:61px">
      <span class="wide" style="font-size:48px;letter-spacing:3px;line-height:1">SALE</span>
    </div>
    <div class="line slant" style="top:212px;font-size:27px;color:var(--green)">Detox this SUMMER</div>
    <div class="line slant" style="top:242px;font-size:27px;color:var(--green-dark)">Shine this SUMMER</div>
  </section>

  <!-- 10 -->
  <section class="panel row-2 col-5">
    <div class="big-25" style="left:18px;top:25px;font-size:100px;color:var(--green)">25</div>
    <div class="pct" style="left:152px;top:25px;font-size:56px;color:var(--green)">%</div>
    <div class="off-small" style="left:152px;top:78px;font-size:25px;color:var(--green)">OFF</div>
    <div class="line slant" style="top:109px;font-size:28px;color:var(--green-dark)">MOTHER’S DAY SALE</div>
    <div class="line serif-spring" style="top:126px;font-size:54px">SPRING</div>
    <div class="photo" role="img" aria-label="Small white supplement bottle" style="left:16px;top:180px;width:22px;height:40px;border-radius:4px"></div>
    <div class="photo" role="img" aria-label="Small white supplement bottle" style="left:192px;top:180px;width:22px;height:40px;border-radius:4px"></div>
    <div class="line slant" style="top:186px;font-size:31px;color:var(--green)">DETOX FOR A</div>
    <div class="line slant" style="top:219px;font-size:37px;color:var(--green-dark)">SUMMER BODY</div>
  </section>

</main>
</body>
</html>
```